■目的・概要 ・QMRへの出稿用バナー作成をしていただける方を募集します。 ---------------- ■注意点 ご提案頂きましたバナー案について、SNSへの投稿・Webサイトへのアップ等を行わないようにお願いします。 採用前後に若干の修正もしくは大きな修正が発生する場合がございます。 ※承諾頂ける方のみコンペへの参加をお願いします。 ---------------- ■依頼詳細 ・バナー内にテキストを挿入する場合は、テキストレイヤーで挿入してください。 ・テキストはおよそ1/4サイズで表示される事を考慮して制作して下さい。 ・配信時は制作したバナーがスマホの画面幅程度に縮小されて表示されます。テキストの可読性を考慮して制作お願いします ・バナー広告を見て、押したくなるようなバナー作成をお願いします。 ■ 参考サイト(配信サイト) https://www.kabeno-hifuka.example/ ※対応方法の一部変更(9/27内容修正) ・コンペは今まで通り、1200×628 で行います。 ・採用になった作品の納品時に300×300のバナーを作成して頂き一緒に納品して頂きたいです ※300×300のバナーは採用バナーの簡易版としてつけて頂けると幸いです。 ⇒そのまま縮小というより、「メイン画像+社名(ロゴ)+一言キャッチ」くらい簡易的でOKです。 小さいバナーですので可読性を考慮して頂けると幸いです。 ■サイズと枚数 【コンペ】 ・1200 x 628 ・1枚 【納品時】 ・1200 x 628 → 1枚 ・300×300→ 1枚 ■納品ファイル ・フォトショップ形式(.psd) ■注意点・禁止事項 土日・祝日は対応することができません。 平日は9~18時までにご連絡いただければ、当日。 それ以降は翌日にご返信いたします。 ※Zelbo QMRガイドラインに沿った内容である事 QMR掲載ガイドライン関連資料(http://adguide.zelbo-example.jp/online/doc/pdf_guideline.html) ※他で登録されているデザインや商標の転用など、他社の知的財産権を侵すこと ※他のクライアントへ既に提案した内容の転用など たくさんのウェブデザイナーの方からのご提案をお待ちしております。 |
クライアント様が気に入りましたので、採用致します。
これからも沢山募集しますので、よろしくお願い致します。

```html
<!DOCTYPE html>
<html lang="ja">
<head>
<meta charset="utf-8">
<title>壁野皮膚科医院 バナー</title>
<link rel="stylesheet" href="https://fonts.googleapis.com/css2?family=Shippori+Mincho:wght@400;500&display=swap">
<style>
  :root {
    --paper: #ffffff;
    --ink: #3b3230;
    --band: #3e342b;
    --band-edge: #8a7a63;
    --band-text: #ffffff;
    --rose-deep: #e59bab;
    --rose-mid: #f4c7cf;
    --rose-light: #fbe6ea;
    --photo-warm: #d9b49a;
    --photo-shade: #6e4d3c;
    --photo-light: #f2e7df;
  }
  * { margin: 0; padding: 0; box-sizing: border-box; }
  html, body { width: 1200px; height: 628px; overflow: hidden; background: var(--paper); }
  .banner {
    position: relative;
    width: 1200px;
    height: 628px;
    overflow: hidden;
    background: var(--paper);
    font-family: "Shippori Mincho", "Noto Serif JP", serif;
    color: var(--ink);
  }
  .roses {
    position: absolute;
    left: 0; top: 0;
    width: 420px; height: 544px;
    background:
      radial-gradient(circle at 60px 80px, var(--rose-mid) 0 60px, transparent 110px),
      radial-gradient(circle at 70px 330px, var(--rose-deep) 0 55px, transparent 120px),
      radial-gradient(circle at 180px 200px, var(--rose-light) 0 70px, transparent 130px),
      radial-gradient(circle at 30px 480px, var(--rose-mid) 0 50px, transparent 100px),
      linear-gradient(90deg, var(--rose-mid) 0%, var(--rose-light) 45%, rgba(255,255,255,0) 100%);
  }
  .family-photo {
    position: absolute;
    right: 0; top: 0;
    width: 420px; height: 544px;
    background:
      radial-gradient(ellipse at 70% 40%, var(--photo-warm) 0%, rgba(217,180,154,0) 60%),
      radial-gradient(ellipse at 85% 15%, var(--photo-shade) 0%, rgba(110,77,60,0) 45%),
      linear-gradient(90deg, rgba(242,231,223,0) 0%, var(--photo-light) 35%, var(--photo-warm) 100%);
  }
  .clinic-name {
    position: absolute;
    left: 0; width: 1200px;
    top: 160px;
    padding-left: 10px;
    text-align: center;
    font-size: 74px;
    font-weight: 500;
    letter-spacing: 6px;
    line-height: 1;
  }
  .tagline {
    position: absolute;
    left: 0; width: 1200px;
    top: 300px;
    padding-left: 110px;
    text-align: center;
    font-size: 40px;
    line-height: 78px;
    letter-spacing: 2px;
  }
  .tagline span { display: block; }
  .tagline .line-1 { padding-right: 80px; }
  .info-band {
    position: absolute;
    left: 0; bottom: 0;
    width: 1200px; height: 86px;
    background: var(--band);
    border-top: 4px solid var(--band-edge);
    color: var(--band-text);
    font-size: 36px;
    letter-spacing: 1px;
    display: flex;
    align-items: center;
    justify-content: center;
  }
</style>
</head>
<body>
  <div class="banner">
    <div class="roses" role="img" aria-label="淡いピンクのバラの花束の写真"></div>
    <div class="family-photo" role="img" aria-label="笑顔の母親が幼い男の子を抱いている写真"></div>
    <h1 class="clinic-name">壁野皮膚科医院</h1>
    <p class="tagline">
      <span class="line-1">お子様からお年寄りまで、</span>
      <span class="line-2">皮膚のトラブル、何でもご相談ください。</span>
    </p>
    <div class="info-band">《予約制》みなと市壁野ショッピングセンター２階</div>
  </div>
</body>
</html>
```